Valtrin Global Wordpress website design

We need a worddpress website/theme design for a new outsourcing company based in Australia.Name of the company is "Valtrin".
Website content is in progress.
The design needs to be clean without clutter in any section. Some example websites are provided below
Menu
- Resources
- Services
- Our difference
Home page needs to have a gif image, for example http://www.brelvana.com. or http://www.qorthello.com or http://www.qorthello.com/team.html
We like how the qorthello website flows without having the need to click on the menu. It is also mobile friendly (which is important)
Each piece of content will have a learn more button
A call to action button will be placed on the home page, which will provide our phone number and access to online form*
A call to action button will also be added to various other pages such as Resources.
Resources Section will contain web articles, whitepapers, blog and any other ccontent which helps customer in making a decision
Having the ability to add a video or images on the home page is also important
Ability to edit the content easily via wordpress is extremely important
* This is a great Contact Us form - http://www.lumtasko.com/#/schedule-meeting
* We do not need the traditional web form on the contact us page
Target Market(s)
Small to medium businesses requiring outsourcing services
Industry/Entity Type
It Company
Coding
Coded - Design and coding required
Colors
Designer to choose colors to be used in the design.
Look and feel

```html
<!DOCTYPE html>
<html lang="en">
<head>
<meta charset="utf-8">
<title>Valtrin Global</title>
<link href="https://fonts.googleapis.com/css2?family=Open+Sans:wght@400;600;700;800&display=swap" rel="stylesheet">
<style>
:root{
  --red:#e5343b;
  --hero:#5f93c6;
  --hero-dark:#4a7fb5;
  --ink:#2b2b2b;
  --muted:#555;
  --panel:#f3f3f3;
  --dark:#141414;
  --footer:#3a3a3a;
  --bottom:#222;
  --orange:#f58a2a;
  --white:#fff;
}
*{box-sizing:border-box;margin:0;padding:0}
html,body{width:1200px;height:3120px;overflow:hidden}
body{font-family:"Open Sans",Arial,sans-serif;color:var(--ink);background:var(--white);position:relative}
.abs{position:absolute}
.btn-outline{position:absolute;border:2px solid var(--red);color:var(--red);font-size:13px;font-weight:600;letter-spacing:.5px;display:flex;align-items:center;justify-content:center;text-transform:uppercase;background:transparent}
.btn-solid{position:absolute;background:var(--red);color:var(--white);font-size:13px;font-weight:700;display:flex;align-items:center;justify-content:center;text-transform:uppercase}

/* hero */
.hero{position:absolute;left:0;top:0;width:1200px;height:661px;background:linear-gradient(180deg,var(--hero) 0%,#6a9dcd 60%,#7aa8d4 100%)}
.logo{position:absolute;font-weight:600;color:var(--white);letter-spacing:6px}
.hero .logo{left:75px;top:44px;font-size:40px}
.phone{position:absolute;left:752px;top:54px;color:var(--white);font-size:17px;font-weight:600;display:flex;align-items:center;gap:7px}
.contact-btn{left:936px;top:48px;width:121px;height:35px;font-size:14px}
.menu-icon{position:absolute;left:1094px;top:52px;width:32px}
.menu-icon span{display:block;height:4px;background:var(--white);margin-bottom:6px;border-radius:1px}
.hero h1{position:absolute;left:74px;top:226px;font-size:55px;font-weight:800;color:var(--white);letter-spacing:1px}
.hero .lede{position:absolute;left:77px;top:294px;width:420px;font-size:23px;line-height:28px;font-weight:700;color:var(--white)}
.play{position:absolute;left:76px;top:400px}
.play-btn{position:absolute;left:75px;top:472px;width:214px;height:46px;background:#4b6d8f;border:2px solid #a9c3dc;color:var(--white);font-size:14px;font-weight:600;display:flex;align-items:center;justify-content:center}
.hero-art{position:absolute;left:530px;top:160px;width:570px;height:410px;border-radius:8px;background:linear-gradient(135deg,rgba(255,255,255,.22),rgba(40,70,120,.25))}

/* pattern bands */
.pattern{position:absolute;background:linear-gradient(135deg,#f8c14a 0%,var(--orange) 45%,#f04c3e 100%)}
.panel{position:absolute;background:var(--panel)}
.panel h2{text-align:center;font-size:27px;font-weight:400;letter-spacing:1px;color:var(--ink)}
.panel p{text-align:center;font-size:14.5px;line-height:26.5px;color:var(--muted)}

/* services */
.services{position:absolute;left:0;top:1073px;width:1200px;height:452px;background:var(--dark)}
.services h2{position:absolute;top:44px;width:100%;text-align:center;color:var(--white);font-size:27px;font-weight:400;letter-spacing:1px}
.service-card{position:absolute;top:119px;width:331px;height:266px;border:1px solid #6a6a6a;background:#1a1a1a}
.service-card .icon{position:absolute;left:128px;top:20px;width:76px;height:76px;border:2px solid var(--red);border-radius:50%;display:flex;align-items:center;justify-content:center}
.service-card h3{position:absolute;top:126px;width:100%;text-align:center;color:var(--white);font-size:15px;line-height:19px;font-weight:700;letter-spacing:.5px}
.service-card p{position:absolute;top:170px;width:100%;text-align:center;color:#d8d8d8;font-size:14px;line-height:22px}
.service-card .btn-solid{left:98px;top:246px;width:133px;height:37px;font-size:12px}

/* articles */
.col-title{position:absolute;top:1958px;font-size:27px;font-weight:400;letter-spacing:.5px;color:var(--ink)}
.item-img{position:absolute;width:179px;height:125px}
.item-title{position:absolute;font-size:15px;font-weight:700;color:var(--red);letter-spacing:.3px}
.item-text{position:absolute;width:300px;font-size:13.5px;line-height:22px;color:var(--muted)}
.item-meta{position:absolute;font-size:13px;font-weight:700;color:var(--ink)}

/* difference */
.difference{position:absolute;left:0;top:2454px;width:1200px;height:337px;background:#f2f2f2}
.difference-art{position:absolute;left:62px;top:40px;width:416px;height:297px;border-radius:200px 200px 0 0;background:linear-gradient(180deg,#d6e8f4,#b9d6ea)}
.difference h2{position:absolute;left:526px;top:62px;font-size:27px;font-weight:400;letter-spacing:.5px}
.difference p{position:absolute;left:526px;top:112px;width:590px;font-size:14px;line-height:27px;color:var(--muted)}

/* footer */
.footer{position:absolute;left:0;top:2791px;width:1200px;height:260px;background:var(--footer);color:#ddd}
.footer .logo{left:75px;top:48px;font-size:44px}
.footer .about{position:absolute;left:75px;top:118px;width:350px;font-size:13.5px;line-height:23px;color:#e4e4e4}
.footer h4{position:absolute;font-size:12.5px;font-weight:700;letter-spacing:1px;color:var(--white)}
.footer ul{position:absolute;left:472px;top:84px;list-style:none}
.footer li{font-size:13px;line-height:29.5px;color:#d4d4d4}
.email{position:absolute;left:705px;top:92px;width:277px;height:44px;background:var(--white);color:#444;font-size:13px;padding-left:16px;display:flex;align-items:center}
.footer .btn-solid{left:992px;top:92px;width:106px;height:44px;font-size:13px}
.social{position:absolute;left:705px;top:206px;display:flex;gap:22px}
.social span{width:20px;height:20px;background:#9a9a9a;border-radius:3px}
.bottom{position:absolute;left:0;top:3051px;width:1200px;height:69px;background:var(--bottom);color:#a8a8a8;font-size:12.5px;display:flex;align-items:center;justify-content:center}
</style>
</head>
<body>

<section class="hero">
  <div class="logo">VALTRIN</div>
  <div class="phone">
    <svg width="16" height="16" viewBox="0 0 24 24"><path fill="#fff" d="M6.6 10.8a15.1 15.1 0 0 0 6.6 6.6l2.2-2.2c.3-.3.7-.4 1-.2 1.1.4 2.3.6 3.6.6.6 0 1 .4 1 1V20c0 .6-.4 1-1 1A17 17 0 0 1 3 4c0-.6.4-1 1-1h3.5c.6 0 1 .4 1 1 0 1.3.2 2.5.6 3.6.1.3 0 .7-.2 1z"/></svg>
    1-800-555-0142
  </div>
  <div class="btn-solid contact-btn">Contact Us</div>
  <div class="menu-icon"><span></span><span></span><span></span></div>
  <h1>NAM FERMENTUM</h1>
  <p class="lede">Vestibulum ante ipsum primis in faucibus orci luctus et ultrices posuere..</p>
  <svg class="play" width="54" height="54" viewBox="0 0 54 54"><circle cx="27" cy="27" r="23" fill="none" stroke="#fff" stroke-width="4"/><path d="M21 16 L37 27 L21 38 Z" fill="#fff"/></svg>
  <div class="play-btn">PLAY VIDEO</div>
  <div class="hero-art" role="img" aria-label="Illustration of business people climbing a rising outsourcing chart"></div>
</section>

<!-- welcome -->
<div class="pattern" style="left:0;top:661px;width:327px;height:412px;" role="img" aria-label="Orange and red triangle pattern"></div>
<div class="pattern" style="left:863px;top:661px;width:337px;height:255px;" role="img" aria-label="Orange and red triangle pattern"></div>
<div class="panel" style="left:137px;top:707px;width:926px;height:316px;">
  <h2 style="margin-top:36px">WELCOME TO OUR <b style="font-weight:800">VALTRIN</b></h2>
  <p style="margin:20px 40px 0">Aliquam molestie, mi et imperdiet euismod, dui purus auctor tellus, et interdum lacus lectus et ante. Sed accumsan sollicitudin sapien, sit amet adipiscing turpis gravida ac. In congue, neque ac lobortis volutpat, libero mauris varius mi, vitae suscipit ipsum ligula vitae risus. Duis aliquam nibh a dui iaculis viverra id a velit. Vivamus egestas risus in magna varius commodo. Sed semper viverra egestas. Etiam pretium porttitor lectus, vel ornare neque porta volutpat.</p>
  <div class="btn-outline" style="left:354px;top:221px;width:216px;height:45px;">Learn More</div>
</div>

<!-- services -->
<section class="services">
  <h2>OUR SERVICES</h2>
  <div class="service-card" style="left:75px;">
    <div class="icon"><svg width="30" height="30" viewBox="0 0 24 24" fill="none" stroke="#fff" stroke-width="1.8"><path d="M9 18h6M10 21h4M12 3a6 6 0 0 0-3.5 10.9c.6.5 1 1.2 1 2.1h5c0-.9.4-1.6 1-2.1A6 6 0 0 0 12 3z"/></svg></div>
    <h3>IT OUTSOURCING<br>SOLUTIONS</h3>
    <p>Aliquam molestie, mi et imperdiet euis-<br>mod, dui purus auctor tellus,<br>et interdum lacus lectus..</p>
    <div class="btn-solid">Learn More</div>
  </div>
  <div class="service-card" style="left:435px;">
    <div class="icon"><svg width="32" height="26" viewBox="0 0 32 22"><rect x="1" y="1" width="30" height="20" rx="2" fill="none" stroke="#fff" stroke-width="2"/><circle cx="16" cy="11" r="5" fill="#fff"/></svg></div>
    <h3>FINANCE OUTSOURCING<br>SERVICES</h3>
    <p>Aliquam molestie, mi et imperdiet euis-<br>mod, dui purus auctor tellus,<br>et interdum lacus lectus..</p>
    <div class="btn-solid">Learn More</div>
  </div>
  <div class="service-card" style="left:796px;">
    <div class="icon"><svg width="32" height="28" viewBox="0 0 32 28"><ellipse cx="13" cy="11" rx="12" ry="9" fill="#fff"/><path d="M5 17 L3 24 L11 19 Z" fill="#fff"/><ellipse cx="22" cy="16" rx="9" ry="7" fill="#fff" stroke="#1a1a1a" stroke-width="2"/></svg></div>
    <h3>CALL CENTER OUTSOURCING<br>SERVICES</h3>
    <p>Aliquam molestie, mi et imperdiet euis-<br>mod, dui purus auctor tellus,<br>et interdum lacus lectus..</p>
    <div class="btn-solid">Learn More</div>
  </div>
</section>

<!-- resources -->
<div class="pattern" style="left:0;top:1525px;width:327px;height:389px;" role="img" aria-label="Orange and red triangle pattern"></div>
<div class="pattern" style="left:863px;top:1525px;width:337px;height:245px;" role="img" aria-label="Orange and red triangle pattern"></div>
<div class="panel" style="left:137px;top:1575px;width:926px;height:287px;">
  <h2 style="margin-top:34px">RESOURCES</h2>
  <p style="margin:18px 40px 0">Aliquam molestie, mi et imperdiet euismod, dui purus auctor tellus, et interdum lacus lectus et ante. Sed accumsan sollicitudin sapien, sit amet adipiscing turpis gravida ac. In congue, neque ac lobortis volutpat, libero mauris varius mi, vitae suscipit ipsum ligula vitae risus. Duis aliquam nibh a dui iaculis viverra id a velit.</p>
  <div class="btn-outline" style="left:354px;top:195px;width:216px;height:45px;">Learn More</div>
</div>

<!-- whitepapers & blog -->
<h2 class="col-title" style="left:75px;">WHITEPAPERS</h2>
<h2 class="col-title" style="left:615px;">BLOG POSTS</h2>

<div class="item-img" style="left:75px;top:2022px;background:linear-gradient(135deg,#e9eef2,#9fc4dc);" role="img" aria-label="Photo of a desk with a tablet and notebook"></div>
<div class="item-title" style="left:268px;top:2018px;">ALIQUAM MOLESTIE</div>
<p class="item-text" style="left:268px;top:2045px;">Dui purus auctor tellus, et interdum lacus lectus et ante nibh eget turpis vehicula tempus ac sed viverra...</p>
<div class="item-meta" style="left:268px;top:2125px;">Read More</div>

<div class="item-img" style="left:75px;top:2190px;background:linear-gradient(135deg,#cfc9c0,#6d6a66);" role="img" aria-label="Photo of hands typing on a laptop"></div>
<div class="item-title" style="left:268px;top:2186px;">ALIQUAM MOLESTIE</div>
<p class="item-text" style="left:268px;top:2213px;">Dui purus auctor tellus, et interdum lacus lectus et ante nibh eget turpis vehicula tempus ac sed viverra...</p>
<div class="item-meta" style="left:268px;top:2293px;">Read More</div>

<div class="item-img" style="left:615px;top:2022px;background:linear-gradient(135deg,#5a6470,#2f3640);" role="img" aria-label="Photo of colleagues working at computers"></div>
<div class="item-title" style="left:808px;top:2018px;">ALIQUAM MOLESTIE</div>
<p class="item-text" style="left:808px;top:2045px;">Dui purus auctor tellus, et interdum lacus lectus et ante nibh eget turpis vehicula tempus ac sed viverra...</p>
<div class="item-meta" style="left:808px;top:2125px;">Aug 16, 2017</div>

<div class="item-img" style="left:615px;top:2190px;background:linear-gradient(135deg,#8a8f99,#3e4450);" role="img" aria-label="Photo of a call centre team with headsets"></div>
<div class="item-title" style="left:808px;top:2186px;">ALIQUAM MOLESTIE</div>
<p class="item-text" style="left:808px;top:2213px;">Dui purus auctor tellus, et interdum lacus lectus et ante nibh eget turpis vehicula tempus ac sed viverra...</p>
<div class="item-meta" style="left:808px;top:2293px;">Aug 16, 2017</div>

<div class="btn-outline" style="left:75px;top:2361px;width:214px;height:46px;">Learn More</div>
<div class="btn-outline" style="left:614px;top:2361px;width:216px;height:46px;">Learn More</div>

<!-- difference -->
<section class="difference">
  <div class="difference-art" role="img" aria-label="Illustration of a team gathered around a computer"></div>
  <h2>OUR DIFFERENCE</h2>
  <p>Aliquam molestie, mi et imperdiet euismod, dui purus auctor tellus, et interdum lacus lectus et ante. Sed accumsan sollicitudin sapien, sit amet adipiscing turpis gravida ac. In congue, neque ac lobortis volutpat, libero mauris varius mi..</p>
  <div class="btn-outline" style="left:526px;top:221px;width:217px;height:46px;">Learn More</div>
</section>

<!-- footer -->
<footer class="footer">
  <div class="logo">VALTRIN</div>
  <p class="about">Aliquam molestie, mi et imperdiet euismod, dui purus auctor tellus, et interdum lacus lectus et ante. Sed accumsan sollicitudin sapien, sit amet adipisc-ing turpis gravida ac.</p>
  <h4 style="left:472px;top:54px;">NAVIGATION</h4>
  <ul>
    <li>Home</li><li>Resources</li><li>Services</li><li>Our Difference</li><li>Contact us</li>
  </ul>
  <h4 style="left:705px;top:54px;">SIGN UP FOR UPDATES</h4>
  <div class="email">Enter Email Address</div>
  <div class="btn-solid">Sign Up</div>
  <h4 style="left:705px;top:175px;font-size:12px;">FOLLOW US</h4>
  <div class="social"><span></span><span></span><span></span><span></span><span></span></div>
</footer>
<div class="bottom">Copyright © 2017. Company Name. All Right Reserved</div>

</body>
</html>
```